Tomas Verlund,M.D. Pediatric Office
Stationery, Envelopes and Biz Card
Bright & Fun-filled
Tomas Verlund,M.D.P.C.
Board Certified Pediatrician
3916 Pellingham Rd. Suite 204
Dearborn, MI 48391
tomas@verlundo.example
www.verlundo.example
Please use my logo on top and elements derived from my logo on other parts of stationery:
Suggestions: The boy and girl on the logo could be used in a playing or happy walking position at the bottom of the letterhead above the address and phone number area
and can be used at the addressee's area on the envelope in a wlcoming happy position. (Please feel free to be totally creative. I'm open to all suggestions and innovations).Different is good!!
Elements derived from logo
Be totally free and creative. You are the expert!

```html
<!DOCTYPE html>
<html lang="en">
<head>
<meta charset="utf-8">
<title>Tomas Verlund, M.D., P.C. — Stationery</title>
<link rel="stylesheet" href="https://fonts.googleapis.com/css2?family=Arimo:wght@400;700&display=swap">
<style>
  :root {
    --green-deep: #7dbb2e;
    --green-light: #d9ecae;
    --pink: #f4a49a;
    --yellow: #fde36a;
    --blue: #5ec4e6;
    --ink: #222;
    --brand: #2a86b5;
    --tagline: #e0428a;
    --back-text: #c2354e;
    --rule: #c9c9c9;
    --paper: #fff;
  }
  * { box-sizing: border-box; margin: 0; padding: 0; }
  html, body { width: 1200px; height: 886px; overflow: hidden; background: var(--paper); }
  body { position: relative; font-family: "Arimo", Arial, sans-serif; color: var(--ink); }

  .sheet-label {
    position: absolute; width: 564px; text-align: center;
    font-weight: 700; font-size: 22px; letter-spacing: .5px;
  }
  .card {
    position: absolute; width: 564px; background: var(--paper);
    border: 1px solid #ddd; overflow: hidden;
  }
  .card--tall { height: 413px; }
  .card--short { height: 322px; }

  .band-top {
    position: absolute; left: 0; top: 0; width: 330px; height: 55px;
    background: linear-gradient(90deg, var(--green-deep), var(--green-light));
  }
  .band-bottom {
    position: absolute; right: 0; height: 58px; left: 228px;
    background: linear-gradient(90deg, var(--green-light), var(--green-deep));
  }
  .tile { position: absolute; width: 62px; height: 58px; }
  .tile--pink { background: var(--pink); }
  .tile--yellow { background: var(--yellow); }
  .tile--blue { background: var(--blue); }

  .holder { position: absolute; left: 24px; font-size: 15px; line-height: 19px; }
  .holder strong { font-weight: 700; }

  .brand { position: absolute; display: flex; align-items: center; gap: 12px; }
  .brand-mark { width: 92px; height: 72px; background: var(--blue); }
  .brand-name { color: var(--brand); font-size: 21px; font-weight: 400; line-height: 24px; }
  .brand-tag { color: var(--tagline); font-size: 14px; line-height: 18px; }

  .address { position: absolute; left: 24px; font-size: 13px; line-height: 19px; }
  .phones { position: absolute; left: 430px; font-size: 13px; line-height: 19px; }
  .phones b, .address b { color: var(--tagline); font-weight: 700; }
  .web { position: absolute; left: 365px; font-size: 13px; }

  .mini-mark { position: absolute; left: 24px; top: 79px; width: 110px; height: 84px; background: var(--blue); }
  .stamp { position: absolute; left: 444px; top: 79px; width: 79px; height: 79px; border: 1px solid #999; }
  .address-line { position: absolute; left: 84px; width: 360px; height: 1px; background: var(--rule); }

  .card--back-full { background: linear-gradient(135deg, var(--green-deep), #a6d45a 60%, var(--green-deep)); }
  .back-mark { position: absolute; left: 228px; top: 110px; width: 108px; height: 108px; background: var(--blue); }
  .back-note {
    position: absolute; left: 0; right: 0; top: 238px; text-align: center;
    color: var(--back-text); font-size: 13px; line-height: 21px;
  }
</style>
</head>
<body>

  <div class="sheet-label" style="left:19px; top:14px;">POST CARD FRONT</div>
  <div class="sheet-label" style="left:612px; top:14px;">POST CARD BACK</div>
  <div class="sheet-label" style="left:19px; top:470px;">FRONT</div>
  <div class="sheet-label" style="left:612px; top:470px;">BACK</div>

  <!-- Postcard front -->
  <section class="card card--tall" style="left:19px; top:48px;">
    <div class="band-top"></div>
    <div class="tile tile--pink" style="left:336px; top:0;"></div>
    <div class="tile tile--yellow" style="left:413px; top:0;"></div>
    <div class="tile tile--blue" style="left:490px; top:0; width:74px;"></div>

    <p class="holder" style="top:66px;"><strong>Tomas Verlund, M.D., F.A.A.P.</strong><br>President</p>

    <div class="brand" style="left:96px; top:155px;">
      <div class="brand-mark"></div>
      <div>
        <div class="brand-name">Tomas Verlund, M.D., P.C.</div>
        <div class="brand-tag">Board Certified Pediatrician</div>
      </div>
    </div>

    <p class="address" style="top:276px;">3916 Pellingham Rd. Suite 204<br>Dearborn, MI 48391<br><b>E</b> : tomas@verlundo.example</p>
    <p class="phones" style="top:302px;"><b>P</b> : 313-555-0142<br><b>F</b> : 313-555-0187</p>

    <div class="tile tile--blue" style="left:0; top:355px;"></div>
    <div class="tile tile--yellow" style="left:77px; top:355px; background:#b9d25a;"></div>
    <div class="tile tile--pink" style="left:154px; top:355px;"></div>
    <div class="band-bottom" style="top:355px;"></div>
    <p class="web" style="top:377px;">W : www.verlundo.example</p>
  </section>

  <!-- Postcard back -->
  <section class="card card--tall" style="left:612px; top:48px;">
    <div class="band-top"></div>
    <div class="tile tile--pink" style="left:336px; top:0;"></div>
    <div class="tile tile--yellow" style="left:413px; top:0;"></div>
    <div class="tile tile--blue" style="left:490px; top:0; width:74px;"></div>

    <div class="mini-mark" role="img" aria-label="Practice brand mark"></div>
    <div class="stamp"></div>
    <div class="address-line" style="top:230px;"></div>
    <div class="address-line" style="top:276px;"></div>
    <div class="address-line" style="top:324px;"></div>

    <div class="tile tile--blue" style="left:0; top:355px;"></div>
    <div class="tile tile--yellow" style="left:77px; top:355px;"></div>
    <div class="tile tile--pink" style="left:154px; top:355px;"></div>
    <div class="band-bottom" style="top:355px;"></div>
  </section>

  <!-- Business card front -->
  <section class="card card--short" style="left:19px; top:500px;">
    <div class="band-top"></div>
    <div class="tile tile--pink" style="left:336px; top:0;"></div>
    <div class="tile tile--yellow" style="left:413px; top:0;"></div>
    <div class="tile tile--blue" style="left:490px; top:0; width:74px;"></div>

    <p class="holder" style="top:68px;"><strong>Tomas Verlund, M.D., F.A.A.P.</strong><br>President</p>

    <div class="brand" style="left:96px; top:112px;">
      <div class="brand-mark" style="width:84px; height:64px;"></div>
      <div>
        <div class="brand-name">Tomas Verlund, M.D., P.C.</div>
        <div class="brand-tag">Board Certified Pediatrician</div>
      </div>
    </div>

    <p class="address" style="top:210px;">3916 Pellingham Rd. Suite 204<br>Dearborn, MI 48391<br><b>E</b> : tomas@verlundo.example</p>
    <p class="phones" style="top:229px;"><b>P</b> : 313-555-0142<br><b>F</b> : 313-555-0187</p>

    <div class="tile tile--blue" style="left:0; top:269px; height:53px;"></div>
    <div class="tile tile--yellow" style="left:77px; top:269px; height:53px;"></div>
    <div class="tile tile--pink" style="left:154px; top:269px; height:53px;"></div>
    <div class="band-bottom" style="top:269px; height:53px;"></div>
    <p class="web" style="top:290px;">W : www.verlundo.example</p>
  </section>

  <!-- Business card back -->
  <section class="card card--short card--back-full" style="left:612px; top:500px;">
    <div class="back-mark" role="img" aria-label="Practice brand mark"></div>
    <p class="back-note">Elements derived from logo<br>Be totally free and creative. You are the expert!</p>
  </section>

</body>
</html>
```